Local Electrical company need some kick ass business cards

In need of some in your face design business cards for a family owned electrical service company in Edmonton, Alberta Canada. We provide reliable and trustworthy electrical service for commercial and residential work in the Edmonton and area. We have been in business for 25 years.

Target Market(s)

Residential and commercial electrical

Industry/Entity Type

Business

Contact Information for Business Card

Your welcome to change and modify the brightway electric logo. please include the lightbulb! Our Colours are black and green please stay with that.
Please include a name phone number and address on the card
phone number - 780-318-5062
#22, 418 Maple Cres, St.Albert, Alberta.
Two things that need to be on the card.
"your friendly neighborhood electrictrician"
Commercial & residential electrical repair and service

Colors
9bcb3c

Requirements
Must have
• Light bulb guy Attached
• "your friendly neighborhood electrictrician"
• Commercial & residential electrical repair and service
• phone number - 780-318-5062
• #22, 418 Maple Cres, St.Albert, Alberta.
• Our colours are black and green
Nice to have
• go wild i want something loud

```html
<!DOCTYPE html>
<html lang="en">
<head>
<meta charset="utf-8">
<title>Brightway Electric – Business Cards</title>
<link rel="stylesheet" href="https://fonts.googleapis.com/css2?family=Open+Sans:ital,wght@0,400;0,600;0,800;1,400&display=swap">
<style>
  :root {
    --green: #9bcb3c;
    --black: #0c0c0c;
    --page: #3a3a3c;
    --white: #ffffff;
  }
  * { box-sizing: border-box; margin: 0; padding: 0; }
  html, body {
    width: 1200px; height: 1000px; overflow: hidden;
    background: var(--page);
    font-family: "Open Sans", Arial, sans-serif;
  }
  .card {
    position: absolute; left: 220px;
    width: 760px; height: 434px;
    overflow: hidden;
  }
  .card svg.card-shapes { position: absolute; inset: 0; }
  .card--back { top: 50px; background: var(--black); }
  .card--front { top: 516px; background: var(--green); }

  .back-content {
    position: absolute; inset: 0;
    display: flex; flex-direction: column; align-items: center; justify-content: center;
    text-align: center; color: var(--black);
  }
  .tagline { font-size: 19px; font-weight: 400; margin-bottom: 4px; }
  .services-main { font-size: 30px; font-weight: 800; letter-spacing: 0.5px; line-height: 1.1; text-transform: uppercase; }
  .services-sub { font-size: 23px; font-weight: 800; letter-spacing: 0.5px; line-height: 1.15; text-transform: uppercase; }
  .address { font-size: 20px; font-weight: 400; margin-top: 6px; letter-spacing: 0.5px; }
  .phone { font-size: 24px; font-weight: 800; margin-top: 2px; letter-spacing: 0.5px; }

  .front-content {
    position: absolute; inset: 0;
    display: flex; align-items: center; justify-content: center; gap: 18px;
  }
  .brand-dot {
    flex: none;
    width: 70px; height: 70px; border-radius: 50%;
    background: var(--green);
  }
  .brand-name {
    color: var(--green); font-weight: 800; font-size: 42px;
    line-height: 1; letter-spacing: 0.5px; white-space: nowrap;
  }
</style>
</head>
<body>

  <section class="card card--back" aria-label="Business card back">
    <svg class="card-shapes" viewBox="0 0 760 434" aria-hidden="true">
      <ellipse cx="380" cy="217" rx="345" ry="180" fill="var(--green)"/>
      <path d="M61 189 A320 160 0 0 1 540 78" fill="none" stroke="var(--black)" stroke-width="14" stroke-linecap="round"/>
      <path d="M699 231 A320 160 0 0 1 220 356" fill="none" stroke="var(--black)" stroke-width="14" stroke-linecap="round"/>
    </svg>
    <div class="back-content">
      <p class="tagline">"your friendly neighborhood electrictrician"</p>
      <p class="services-main">Commercial &amp; Residential</p>
      <p class="services-sub">Electrical Repair and Service</p>
      <p class="address">#22, 418 Maple Cres, St.Albert, Alberta.</p>
      <p class="phone">780-318-5062</p>
    </div>
  </section>

  <section class="card card--front" aria-label="Business card front">
    <svg class="card-shapes" viewBox="0 0 760 434" aria-hidden="true">
      <g transform="rotate(-6 380 217)">
        <ellipse cx="380" cy="217" rx="355" ry="190" fill="var(--black)"/>
        <path d="M75 243 A310 150 0 0 1 486 76" fill="none" stroke="var(--green)" stroke-width="14" stroke-linecap="round"/>
        <path d="M685 191 A310 150 0 0 1 274 358" fill="none" stroke="var(--green)" stroke-width="14" stroke-linecap="round"/>
      </g>
    </svg>
    <div class="front-content">
      <span class="brand-dot" aria-hidden="true"></span>
      <p class="brand-name">Brightway Electric</p>
    </div>
  </section>

</body>
</html>
```